brilliant Facebook banner, website banner etc

I need Facebook banner, website banner, for my business - Harbor of Morning Fellowship.
Facebook Banner - Fb Banner Size
Website Banner - Leaderboard 728 x 90px
The business focus is products for women who want to focus on conscious personal growth and developing a personal relationship with the Lord. These individuals are prepared to work with the Holy Spirit to not only unfold their life's plan and purpose, but also to experience an ever deepening relationship with the Lord on a daily basis
Updates
Project Deadline Extended Reason: When I came to this site I didn't realise I had to set this up, was focused on another project. My mistake. Added Saturday, June 6, 2015
Target Market(s)
Individuals looking to Awaken their souls/restore their souls.
Industry/Entity Type
Business
Font styles to use
Requirements
Must have
- Be elegant, think hearts, angels wings etc
- Be original
- Company Logo Attached
Nice to have
- I'm completely open to new ideas, and I love creativity.
Should not have
- I don't like bland and boring.

```html
<!DOCTYPE html>
<html lang="en">
<head>
<meta charset="utf-8">
<title>Harbor of Morning Fellowship – Banners</title>
<link rel="stylesheet" href="https://fonts.googleapis.com/css2?family=Great+Vibes&family=Cormorant+Garamond:ital,wght@1,500;1,600&family=Open+Sans:wght@400&display=swap">
<style>
  :root {
    --canvas-top: #d9dbdc;
    --canvas-mid: #f7f8f8;
    --tab-blue: #1fa3e6;
    --purple: #a21fd6;
    --purple-deep: #7a12a8;
    --blue: #1c9ddf;
    --blue-deep: #0a3f9a;
    --blue-mid: #1a6fd0;
    --ink-dark: #3d2b4a;
    --white: #ffffff;
    --silhouette: #0c0a0d;
  }
  * { margin: 0; padding: 0; box-sizing: border-box; }
  html, body { width: 1200px; height: 1200px; overflow: hidden; }
  body {
    position: relative;
    background: radial-gradient(ellipse at 50% 45%, var(--canvas-mid) 0%, #eceded 45%, var(--canvas-top) 100%);
    font-family: "Cormorant Garamond", Georgia, serif;
  }
  .tab {
    position: absolute;
    left: 38px;
    height: 36px;
    color: var(--white);
    font-family: "Open Sans", Arial, sans-serif;
    font-size: 27px;
    line-height: 36px;
    padding-left: 36px;
    white-space: nowrap;
    background: var(--tab-blue);
    clip-path: polygon(14px 0, calc(100% - 16px) 0, 100% 100%, 0 100%);
    border-radius: 8px 8px 0 0;
  }
  .tab-web { top: 218px; width: 232px; }
  .tab-cover { top: 520px; width: 292px; }

  .banner { position: absolute; left: 33px; overflow: hidden; }
  .banner svg.backdrop { position: absolute; inset: 0; }

  .web-banner { top: 258px; width: 1133px; height: 139px; }
  .cover { top: 563px; width: 1135px; height: 420px; }

  .figure-area {
    position: absolute;
    background: linear-gradient(180deg, #1a141c, var(--silhouette));
  }
  .web-banner .figure-area { left: 0; top: 0; width: 90px; height: 139px; border-radius: 0 40px 0 0; }
  .cover .figure-area { left: 0; top: 22px; width: 140px; height: 398px; border-radius: 0 70px 0 0;
    box-shadow: 0 0 40px 18px rgba(255,255,255,0.55); }

  .script { font-family: "Great Vibes", cursive; font-weight: 400; white-space: nowrap; }

  .web-tagline {
    position: absolute; left: 150px; top: 6px; width: 480px;
    text-align: center; font-size: 44px; color: var(--ink-dark);
  }
  .web-name {
    position: absolute; left: 100px; top: 64px; width: 600px;
    text-align: center; font-size: 52px; color: var(--white);
  }
  .mark-dot {
    position: absolute; border-radius: 50%;
    background: rgba(255,255,255,0.25);
  }
  .web-banner .mark-dot { left: 970px; top: 18px; width: 96px; height: 96px; }

  .cover-copy {
    position: absolute; text-align: center;
    font-style: italic; font-weight: 500; font-size: 27px; line-height: 40px;
  }
  .cover-copy-lead { left: 225px; top: 30px; width: 545px; color: var(--ink-dark); }
  .cover-copy-support { left: 160px; top: 195px; width: 512px; color: var(--white); }

  .cover .mark-dot { left: 900px; top: 140px; width: 170px; height: 170px; }
  .cover-name {
    position: absolute; left: 715px; top: 355px; width: 420px;
    text-align: center; font-size: 38px; line-height: 46px; color: var(--white);
  }
  .leaf-area {
    position: absolute; left: 905px; top: 0; width: 230px; height: 95px;
    background: radial-gradient(ellipse at 60% 30%, rgba(220,230,240,0.55), rgba(220,230,240,0) 70%);
  }
</style>
</head>
<body>

<div class="tab tab-web">Web Banner</div>
<section class="banner web-banner">
  <svg class="backdrop" width="1133" height="139" viewBox="0 0 1133 139">
    <defs>
      <linearGradient id="webPurple" x1="0" y1="0" x2="0" y2="1">
        <stop offset="0" stop-color="#b04fe0"/>
        <stop offset="0.35" stop-color="#f3def9"/>
        <stop offset="0.45" stop-color="#b640e6"/>
        <stop offset="1" stop-color="#7a12a8"/>
      </linearGradient>
      <linearGradient id="webBlue" x1="0" y1="0" x2="1" y2="0">
        <stop offset="0" stop-color="#1780d8"/>
        <stop offset="1" stop-color="#2aa8e8"/>
      </linearGradient>
    </defs>
    <rect width="1133" height="139" fill="url(#webPurple)"/>
    <path d="M820 0 C790 60 730 110 650 139 L1133 139 L1133 0 Z" fill="#0a3f9a"/>
    <path d="M850 0 C820 65 770 110 700 139 L1133 139 L1133 0 Z" fill="#1a6fd0"/>
    <path d="M880 0 C860 60 830 110 780 139 L1133 139 L1133 0 Z" fill="url(#webBlue)"/>
  </svg>
  <div class="figure-area" role="img" aria-label="Silhouette of a kneeling woman in prayer"></div>
  <div class="web-tagline script">Awaken Your Soul</div>
  <div class="web-name script">Harbor of Morning Fellowship</div>
  <div class="mark-dot"></div>
</section>

<div class="tab tab-cover">Facebook Cover</div>
<section class="banner cover">
  <svg class="backdrop" width="1135" height="420" viewBox="0 0 1135 420">
    <defs>
      <linearGradient id="coverPurple" x1="0" y1="0" x2="0" y2="1">
        <stop offset="0" stop-color="#b04fe0"/>
        <stop offset="0.3" stop-color="#e8c6f5"/>
        <stop offset="0.36" stop-color="#f7eafb"/>
        <stop offset="0.42" stop-color="#c05ae8"/>
        <stop offset="1" stop-color="#7a12a8"/>
      </linearGradient>
      <linearGradient id="coverBlue" x1="0" y1="0" x2="1" y2="1">
        <stop offset="0" stop-color="#1f8fdc"/>
        <stop offset="1" stop-color="#27a5e6"/>
      </linearGradient>
    </defs>
    <rect width="1135" height="420" fill="url(#coverPurple)"/>
    <path d="M815 0 C780 150 700 330 520 420 L1135 420 L1135 0 Z" fill="#1a6fd0"/>
    <path d="M850 0 C820 150 750 320 610 420 L1135 420 L1135 0 Z" fill="#0a3f9a"/>
    <path d="M900 0 C875 150 820 330 700 420 L1135 420 L1135 0 Z" fill="url(#coverBlue)"/>
  </svg>
  <div class="figure-area" role="img" aria-label="Silhouette of a kneeling woman in prayer, glowing outline"></div>
  <p class="cover-copy cover-copy-lead">We offer products for women who want to focus on conscious personal growth and developing a personal relationship with the Lord.</p>
  <p class="cover-copy cover-copy-support">We prepare you to work with the Holy Spirit to not only unfold your life's plan and purpose, but also to experience an ever deepening relationship with the Lord on a daily basis</p>
  <div class="leaf-area" role="img" aria-label="Faint swirling leaf ornament"></div>
  <div class="mark-dot"></div>
  <div class="cover-name script">Harbor of Morning Fellowship</div>
</section>

</body>
</html>
```